Sports Supplements Company Needs Label Designs

Hello,

We are a sports supplements company named "Veltrane Forge". We produce a line of sports supplements from pre-workouts products to fat burners and multivitamins. Our competitors include companies like Corvalo Provisions and BrawnKettle. Like most companies in the sports supplements field, we need a standard label design for one product that can be later modified a little to be used for the other products. Initially we need a label design for our "BCAA (Branched-Chain Amino Acids)" product. We would like to add other supplements like glutamine and fat burners, so we need a standard design that can be tweaked a bit. The only difference would be the information and ingredients in the other products, which will be provided.

For the design we would like one that reflects a modern, brand-unique approach. It should communicate trust and quality. Competitors designs to be considered as reference would include KDT Fitness, BrawnKettle, and Quenvira. Photos of their products can be seen online in places like liftharbor.example. We would also like to include a couple of small icons to indicate the respective product's main functions. Similar icons can be seen in TWG Provisions products, as an example. Main qualities of the BCAA is "strength", "recovery", "Muscle Growth". The product's name is BCAA Solvexa.

The package will be white, with an undecided lid color (probably black). Color combinations I have in mind are mixed combinations of any of the following colors: red, white, yellow (some light to darker shades), brown, black, green, and blue. But please this does not have to limit your imagination to the design and colors. These are just ideas from top of my head. Since the company's name is Veltrane Forge, I do like the design to represent some sort of "mechanics": I'd like to have some design that includes watch wheels, and maybe a wrench. I also would like the name of the company to be on the label as well, under the logo.

Other project text details and measurements are provided in an attached word document, along with the logo of the company we like to use. We like the format to be Ai.

We'd like a designer to work with in future products, and build a relationship with. As said earlier, we need to hire a designer to work with and modify similar projects with a fixed amount (~$50) for each additional product.

Industry/Entity Type

It Company

Colors
f37122
f78f20
ffc214
fbed22
9bcb3c
ec1f27
0255a3
ffffff
000000

Requirements
Must have
• Some sort of "mechanics": I'd like to have some design that includes watch wheels, and maybe a wrench.
Nice to have
• Some sort of harmonious color mixes. Mixes of yellow or orange with white, or maybe red and black.
Should not have
• Plain label with no designs.
• A simple design.

```html
<!DOCTYPE html>
<html lang="en">
<head>
<meta charset="utf-8">
<title>BCAA Solvexa – Label</title>
<link href="https://fonts.googleapis.com/css2?family=Russo+One&family=Oswald:wght@500;600&family=Roboto+Condensed:wght@400;700&family=Roboto:wght@400;700&display=swap" rel="stylesheet">
<style>
  :root{
    --bg:#e4e5e7;
    --label:#1c1d1f;
    --panel-divider:#2c2e31;
    --blue:#2f74c6;
    --blue-line:#2a63b0;
    --white:#ffffff;
    --icon-fill:#d9dbde;
    --rule:#5b5e63;
    --facts-ink:#111111;
  }
  *{box-sizing:border-box;margin:0;padding:0}
  html,body{width:1200px;height:1000px;overflow:hidden;background:var(--bg)}
  body{font-family:"Roboto",Arial,sans-serif;color:var(--white)}

  .label{
    position:absolute;left:40px;top:270px;width:1120px;height:460px;
    background:var(--label);display:flex;overflow:hidden;
  }
  .label::before,.label::after{
    content:"";position:absolute;left:0;right:0;height:2px;background:var(--blue-line);
  }
  .label::before{top:28px}
  .label::after{bottom:30px}

  .panel{position:relative;height:100%;overflow:hidden}
  .panel--back-left{width:330px;border-right:1px dashed var(--panel-divider)}
  .panel--front{width:460px;display:flex;flex-direction:column;align-items:center;padding-top:48px}
  .panel--back-right{width:330px;border-left:1px dashed var(--panel-divider);padding:50px 26px 0 24px}

  /* front */
  .brand{display:flex;align-items:center;gap:8px;font-family:"Oswald",sans-serif;font-weight:500;font-size:13px;letter-spacing:1px;text-transform:uppercase}
  .brand__dot{width:10px;height:10px;border-radius:50%;background:var(--white)}
  .product-name{margin-top:14px;font-family:"Russo One",sans-serif;font-weight:400;font-size:104px;line-height:1;letter-spacing:4px;color:var(--white)}
  .product-sub{margin-top:6px;font-family:"Oswald",sans-serif;font-weight:500;font-size:27px;letter-spacing:12px;padding-left:12px}
  .benefits{margin-top:14px;width:440px;display:flex;border-top:1px solid var(--rule);border-bottom:1px solid var(--rule);padding:8px 0}
  .benefit{flex:1;text-align:center;border-left:1px solid var(--rule)}
  .benefit:first-child{border-left:none}
  .benefit__verb{font-family:"Oswald",sans-serif;font-weight:600;font-size:15px;letter-spacing:.5px}
  .benefit__target{font-family:"Roboto Condensed",sans-serif;font-size:13px;color:var(--blue);text-transform:uppercase}
  .benefit--main .benefit__verb{font-size:17px}
  .benefit--main .benefit__target{font-size:15px}
  .icons{margin-top:18px;display:flex;gap:46px}
  .icon-slot{width:54px;height:54px;border-radius:50%;background:var(--icon-fill)}
  .pack-info{margin-top:16px;text-align:center;font-size:13px;text-transform:uppercase;line-height:1.3}
  .pack-info strong{font-weight:700}

  /* back left */
  .wrap-name{position:absolute;left:-120px;top:100px;font-family:"Russo One",sans-serif;font-size:72px;line-height:1;color:var(--white);white-space:nowrap}
  .wrap-sub{position:absolute;left:-60px;top:178px;font-family:"Oswald",sans-serif;font-weight:500;font-size:18px;letter-spacing:8px;white-space:nowrap}
  .facts-col{position:absolute;left:128px;top:46px;width:180px}
  .facts{background:var(--white);color:var(--facts-ink);border:2px solid var(--facts-ink);padding:5px 6px;font-size:8px}
  .facts__title{font-size:15px;line-height:1.1}
  .facts__serving{font-size:8px;border-bottom:4px solid var(--facts-ink);padding-bottom:2px}
  .facts__row{display:flex;justify-content:space-between;border-bottom:1px solid #999;padding:3px 0}
  .facts__row--head{border-bottom:2px solid var(--facts-ink);font-size:7px}
  .facts__blank{height:14px;border-bottom:1px solid #999}
  .small-copy{margin-top:8px;font-size:8px;line-height:1.35}
  .small-copy b{font-weight:700}
  .warning{margin-top:10px;font-size:7.5px;font-weight:700;line-height:1.4;text-transform:uppercase;text-align:justify}
  .use-box{margin-top:10px;border:1px solid var(--blue);padding:4px 6px;font-size:8px;line-height:1.35}
  .use-box__title{color:var(--blue);font-weight:700;text-transform:uppercase;text-decoration:underline}
  .side-benefits{position:absolute;left:24px;top:268px;width:96px}
  .side-benefits .benefit__verb{font-size:12px}
  .side-benefits .benefit__target{font-size:10px}
  .side-icon{position:absolute;left:44px;top:322px;width:38px;height:38px;border-radius:50%;background:var(--icon-fill)}

  /* back right */
  .mini-name{font-family:"Russo One",sans-serif;font-size:26px;line-height:1;color:var(--white)}
  .mini-sub{font-family:"Oswald",sans-serif;font-size:9px;letter-spacing:5px;margin:3px 0 6px}
  .body-copy{font-size:8.5px;line-height:1.45;text-align:justify;margin-bottom:12px}
  .body-copy--italic{font-style:italic;font-size:7.5px}
  .company{margin-top:12px;display:flex;gap:10px;align-items:flex-start}
  .company__dot{width:14px;height:14px;border-radius:50%;background:var(--white);margin-top:3px;flex:none}
  .company__name{font-family:"Oswald",sans-serif;font-weight:500;font-size:15px;letter-spacing:.5px;text-transform:uppercase}
  .company__web{font-size:8px;letter-spacing:2px}
  .company__line{display:flex;justify-content:space-between;font-size:7.5px;margin-top:3px;width:220px}
  .company__foot{margin-top:6px;font-size:7px;text-transform:uppercase;letter-spacing:.3px;border-top:1px solid var(--rule);padding-top:3px}
</style>
</head>
<body>
<main class="label">

  <section class="panel panel--back-left" aria-label="Label back, supplement facts">
    <div class="wrap-name" aria-hidden="true">BCAA</div>
    <div class="wrap-sub" aria-hidden="true">SOLVEXA</div>
    <div class="side-benefits">
      <div class="benefit__verb">SUPPORTS</div>
      <div class="benefit__target">Muscle Recovery</div>
    </div>
    <div class="side-icon" role="img" aria-label="Muscle recovery icon"></div>
    <div class="facts-col">
      <div class="facts">
        <div class="facts__title">Supplement Facts</div>
        <div class="facts__serving">Serving Size: 3 Tablets</div>
        <div class="facts__row facts__row--head"><span>Amount Per Serving</span></div>
        <div class="facts__row facts__row--head"><span></span><span>Amount &nbsp;%Daily Value</span></div>
        <div class="facts__row"><span>L-Leucine</span><span>1500 mg &nbsp;*</span></div>
        <div class="facts__row"><span>L-Isoleucine</span><span>750 mg &nbsp;*</span></div>
        <div class="facts__row"><span>L-Valine</span><span>750 mg &nbsp;*</span></div>
        <div class="facts__blank"></div>
        <div class="facts__blank"></div>
      </div>
      <p class="small-copy"><b>Other Ingredients:</b> Calcium carbonate, vegetable stearic acid, hydroxypropyl methylcellulose, vegetable magnesium stearate and silicon dioxide.</p>
      <p class="warning">Keep out of the reach of children. Do not use if safety seal is damaged or missing. Store in a cool, dry place.</p>
      <div class="use-box">
        <div class="use-box__title">Suggested Use:</div>
        1 serving before and/or after training or as directed by a healthcare professional.
      </div>
    </div>
  </section>

  <section class="panel panel--front" aria-label="Label front">
    <div class="brand"><span class="brand__dot"></span>Veltrane Forge</div>
    <h1 class="product-name">BCAA</h1>
    <div class="product-sub">SOLVEXA</div>
    <div class="benefits">
      <div class="benefit">
        <div class="benefit__verb">STIMULATES</div>
        <div class="benefit__target">Protein Synthesis</div>
      </div>
      <div class="benefit benefit--main">
        <div class="benefit__verb">REDUCES</div>
        <div class="benefit__target">Muscle Breakdown</div>
      </div>
      <div class="benefit">
        <div class="benefit__verb">SUPPORTS</div>
        <div class="benefit__target">Muscle Recovery</div>
      </div>
    </div>
    <div class="icons">
      <div class="icon-slot" role="img" aria-label="Strength icon"></div>
      <div class="icon-slot" role="img" aria-label="Muscle breakdown icon"></div>
      <div class="icon-slot" role="img" aria-label="Muscle recovery icon"></div>
    </div>
    <div class="pack-info">Dietary Supplement<br><strong>120</strong> Tablets</div>
  </section>

  <section class="panel panel--back-right" aria-label="Label back, directions and company">
    <div class="mini-name">BCAA</div>
    <div class="mini-sub">SOLVEXA</div>
    <p class="body-copy">Branched chain amino acids help your muscles rebuild after hard training. Each serving delivers leucine, isoleucine and valine in a proven ratio to fuel strength, speed recovery and protect lean muscle during every phase of your program.</p>
    <p class="body-copy body-copy--italic">Do not exceed recommended dose. Not recommended for individuals with allergies to dairy or egg products and should not be used by pregnant or nursing mothers or children under 18 years of age without advice from a physician. This product is manufactured and packaged in a facility which may also process milk, soy, wheat, egg, peanuts, tree nuts, fish and crustacean shellfish.</p>
    <p class="body-copy body-copy--italic">These statements have not been evaluated by the Food and Drug Administration. This product is not intended to diagnose, treat, cure, or prevent any disease.</p>
    <div class="company">
      <span class="company__dot"></span>
      <div>
        <div class="company__name">Veltrane Forge</div>
        <div class="company__web">veltraneforge.example</div>
        <div class="company__line"><span>Harbor City, FL 00000 USA</span><span>800-555-0147</span></div>
        <div class="company__foot">Distributed by Veltrane Forge | Manufactured in a cGMP certified facility</div>
      </div>
    </div>
  </section>

</main>
</body>
</html>
```